Creative & Professional Business Card for hair salon

We are looking to update our business cards. Our salon is creative, modern, progressive and professional and looking for a design that will reflect this.

```html
<!DOCTYPE html>
<html lang="en">
<head>
<meta charset="utf-8">
<title>Silver Loft – Business Cards</title>
<link rel="stylesheet" href="https://fonts.googleapis.com/css2?family=Lato:wght@300;400&display=swap">
<style>
  :root {
    --backdrop: #1c1c1d;
    --card: #2a2a2b;
    --card-edge: #333334;
    --silver: #a9a9ab;
    --sky: #7fb6cc;
    --ink: #f2f2f2;
  }
  * { margin: 0; padding: 0; box-sizing: border-box; }
  html, body {
    width: 1200px;
    height: 900px;
    overflow: hidden;
    background: var(--backdrop);
    font-family: "Lato", sans-serif;
  }
  .sheet {
    width: 1200px;
    height: 900px;
    display: flex;
    flex-direction: column;
    align-items: center;
    justify-content: center;
    gap: 32px;
  }
  .card {
    width: 700px;
    height: 400px;
    background: linear-gradient(135deg, var(--card) 0%, var(--card-edge) 60%, var(--card) 100%);
    position: relative;
  }
  .card-front {
    display: flex;
    align-items: center;
    justify-content: center;
  }
  .wordmark {
    font-weight: 300;
    line-height: 1.1;
    text-align: right;
  }
  .wordmark-name { display: block; font-size: 44px; }
  .wordmark-by { display: block; font-size: 20px; margin-top: 6px; }
  .card-front .wordmark { color: var(--silver); }
  .card-back .wordmark { color: var(--sky); }
  .card-back .wordmark-name { font-size: 36px; }
  .card-back .wordmark-by { font-size: 17px; }
  .card-back .wordmark {
    position: absolute;
    left: 70px;
    top: 142px;
  }
  .divider {
    position: absolute;
    left: 392px;
    top: 86px;
    width: 2px;
    height: 232px;
    background: var(--sky);
  }
  .contact {
    position: absolute;
    left: 430px;
    top: 84px;
    color: var(--ink);
  }
  .contact-name { color: var(--sky); font-size: 27px; font-weight: 400; }
  .contact-role { font-size: 17px; margin-top: 2px; }
  .contact-address { font-size: 17px; line-height: 1.3; margin-top: 14px; }
  .contact-list { list-style: none; margin-top: 16px; font-size: 17px; }
  .contact-list li { display: flex; align-items: center; gap: 10px; height: 26px; }
  .contact-list svg { width: 13px; height: 13px; flex: none; }
  .accent { color: var(--sky); }
</style>
</head>
<body>
<main class="sheet">
  <section class="card card-front" aria-label="Card front">
    <p class="wordmark">
      <span class="wordmark-name">Silver Loft</span>
      <span class="wordmark-by">by Nina Calder</span>
    </p>
  </section>

  <section class="card card-back" aria-label="Card back">
    <p class="wordmark">
      <span class="wordmark-name">Silver Loft</span>
      <span class="wordmark-by">by Nina Calder</span>
    </p>
    <div class="divider"></div>
    <div class="contact">
      <h1 class="contact-name">Jonah Pierce</h1>
      <p class="contact-role">Founder</p>
      <p class="contact-address">5/27 Harbour Lane,<br>Kenmore</p>
      <ul class="contact-list">
        <li>
          <svg viewBox="0 0 16 16" aria-hidden="true"><path d="M4 1 L6.5 4.5 L5 6.5 Q6.5 9.5 9.5 11 L11.5 9.5 L15 12 L13 15 Q6 14 1 3 Z" fill="none" stroke="#c9c9c9" stroke-width="1.4"/></svg>
          07 5123 4890
        </li>
        <li>
          <svg viewBox="0 0 16 16" aria-hidden="true"><rect x="1" y="3" width="14" height="10" fill="none" stroke="#c9c9c9" stroke-width="1.4"/><path d="M1 3 L8 9 L15 3" fill="none" stroke="#c9c9c9" stroke-width="1.4"/></svg>
          salon@silverloft.com.au
        </li>
        <li>
          <svg viewBox="0 0 16 16" aria-hidden="true"><circle cx="8" cy="8" r="6.5" fill="none" stroke="#c9c9c9" stroke-width="1.4"/><ellipse cx="8" cy="8" rx="3" ry="6.5" fill="none" stroke="#c9c9c9" stroke-width="1.2"/><path d="M1.5 8 H14.5" stroke="#c9c9c9" stroke-width="1.2"/></svg>
          <span>www.<span class="accent">silverloft</span>.com.au</span>
        </li>
        <li>
          <svg viewBox="0 0 16 16" aria-hidden="true"><circle cx="8" cy="8" r="6" fill="#c9c9c9"/></svg>
          SilverLoftByNinaCalder
        </li>
      </ul>
    </div>
  </section>
</main>
</body>
</html>
```